PebbleLoop screens tidy up

We would like advice on how to better present the following home page and overview pages.

The existing website is functional, but the pages don't appear professionals and pleasing to the eye. We would specifically like feedback on alignment and padding of icons and text to make the screen more appealing and polished.

We are following the quartz design system.

Number of Pages Required

1 page

Font styles to use
Sans Serif
Other font styles liked:
• IBM Plex, Poppins

```html
<!DOCTYPE html>
<html lang="en">
<head>
<meta charset="utf-8">
<title>PebbleLoop – Home</title>
<link href="https://fonts.googleapis.com/css2?family=IBM+Plex+Sans:wght@400;500;600;700&display=swap" rel="stylesheet">
<style>
:root{
  --navy:#0d1546;
  --orange:#f9a028;
  --orange-deep:#e8841a;
  --page:#e3e3e3;
  --card:#f9f9f9;
  --track:#dedede;
  --muted:#c9ccd8;
}
*{box-sizing:border-box;margin:0;padding:0}
html,body{width:1200px;height:675px;overflow:hidden}
body{font-family:"IBM Plex Sans",sans-serif;background:var(--page);color:var(--navy);position:relative}
.sidebar{position:absolute;left:0;top:0;width:214px;height:675px;background:var(--navy);color:#fff;overflow:hidden}
.brand{position:absolute;left:20px;top:30px;display:flex;align-items:center;gap:9px;font-size:20px;font-weight:600;letter-spacing:-.3px}
.brand-dot{width:22px;height:22px;border-radius:50%;background:var(--orange)}
.nav-item{position:absolute;left:21px;display:flex;align-items:center;gap:9px;font-size:11.5px;font-weight:500}
.nav-item svg{width:10px;height:10px}
.nav-item.active{color:var(--orange);font-weight:600;font-size:12.5px}
.active-bar{position:absolute;left:0;top:96px;width:3px;height:12px;background:var(--orange)}
.badge{position:absolute;left:161px;top:129px;background:var(--orange);color:#fff;font-size:10px;padding:1px 5px;border-radius:9px}
.divider{position:absolute;left:20px;top:196px;width:174px;border-top:1px dashed #3c456e}
.section-label{position:absolute;left:20px;top:212px;font-size:11.5px;font-weight:500}
.section-plus{position:absolute;left:184px;top:210px;font-size:14px;font-weight:400}
.caret{position:absolute;left:186px;width:0;height:0;border-left:3.5px solid transparent;border-right:3.5px solid transparent;border-top:4px solid #fff}
.hive-art{position:absolute;left:0;top:545px;width:214px;height:130px;background:linear-gradient(180deg,rgba(249,160,40,0) 0%,rgba(249,160,40,.55) 45%,var(--orange-deep) 100%)}
.page-title{position:absolute;left:246px;top:32px;font-size:20px;font-weight:600}
.page-title::after{content:"";position:absolute;left:0;bottom:-1px;width:12px;height:2px;background:var(--orange)}
.welcome{position:absolute;left:1076px;top:14px;display:flex;align-items:center;gap:7px}
.avatar{width:27px;height:27px;border-radius:50%;border:2px solid var(--orange);position:relative;background:#fff}
.avatar::after{content:"";position:absolute;right:-2px;bottom:-1px;width:6px;height:6px;border-radius:50%;background:#3cc25b}
.welcome small{display:block;font-size:8px;letter-spacing:.3px}
.welcome strong{display:block;font-size:10px;font-weight:600}
.heading{position:absolute;display:flex;align-items:center;gap:8px;font-size:12.5px;font-weight:600}
.heading svg{width:14px;height:14px}
.card{position:absolute;background:var(--card);border-radius:4px;box-shadow:0 1px 3px rgba(0,0,0,.12)}
.card-title{font-size:12.5px;font-weight:500}
.team-card{left:245px;top:101px;width:924px;height:80px;padding:10px 15px}
.team-card p{font-size:10.5px;margin-top:11px}
.usage-card{left:245px;top:224px;width:566px;height:149px;padding:10px 16px}
.usage-track{position:absolute;left:16px;top:66px;width:534px;height:16px;background:var(--track)}
.usage-fill{width:6px;height:100%;background:var(--orange)}
.usage-note{position:absolute;left:16px;top:113px;font-size:11px}
.stats-card{left:843px;top:224px;width:326px;height:149px;padding:10px 16px}
.stat{position:absolute;top:44px;width:120px;text-align:center}
.stat-num{width:58px;height:58px;margin:0 auto;border-radius:50%;background:var(--orange);display:flex;align-items:center;justify-content:center;font-size:30px;font-weight:700}
.stat-label{margin-top:8px;font-size:11px}
.new-btn{position:absolute;left:1043px;top:392px;width:125px;height:22px;background:var(--orange);color:#fff;font-size:10px;font-weight:500;display:flex;align-items:center;justify-content:center;box-shadow:0 2px 4px rgba(0,0,0,.2)}
.campaign-panel{position:absolute;left:246px;top:420px;width:923px;height:260px;background:var(--card);border-radius:4px}
.campaign{position:absolute;top:438px;width:298px;height:221px;background:#fff;border-radius:5px;box-shadow:0 1px 4px rgba(0,0,0,.1);text-align:center}
.campaign h3{margin-top:20px;font-size:12.5px;font-weight:500}
.campaign .desc{margin-top:10px;font-size:9.5px}
.campaign-art{width:90px;height:72px;margin:8px auto 0;border-radius:36px;background:radial-gradient(circle,var(--orange) 0%,#f6c77c 45%,#e6e6e6 75%,#fff 100%)}
.campaign-count{display:flex;justify-content:center;align-items:flex-end;gap:6px;margin-top:6px;margin-left:-30px}
.campaign-count .num{font-size:34px;font-weight:600;line-height:1}
.campaign-count .txt{text-align:left;line-height:1.25}
.campaign-count small{display:block;font-size:9.5px}
.campaign-count strong{display:block;font-size:11.5px;font-weight:600}
.since{margin-top:16px;font-size:8.5px}
</style>
</head>
<body>
<aside class="sidebar">
  <div class="brand"><span class="brand-dot"></span>PebbleLoop</div>
  <div class="active-bar"></div>
  <div class="nav-item active" style="top:95px"><svg viewBox="0 0 10 10" fill="none" stroke="currentColor"><path d="M1 5 5 1.5 9 5M2.5 4v5h5V4"/></svg>Home</div>
  <div class="nav-item" style="top:129px"><svg viewBox="0 0 10 10" fill="none" stroke="currentColor"><path d="M2 7.5V5a3 3 0 0 1 6 0v2.5H2M4 9h2"/></svg>All Alerts</div>
  <span class="badge">3 new</span>
  <div class="nav-item" style="top:163px"><svg viewBox="0 0 10 10" fill="none" stroke="currentColor"><circle cx="5" cy="5" r="3.5"/><circle cx="5" cy="5" r="1.3"/></svg>Manage</div>
  <div class="divider"></div>
  <div class="section-label">Campaigns</div>
  <div class="section-plus">+</div>
  <div class="nav-item" style="top:244px"><svg viewBox="0 0 10 10" fill="none" stroke="currentColor"><path d="M1 9h8M2 7l5-5 1 1-5 5H2z"/></svg>My Custom Campaigns</div>
  <div class="caret" style="top:251px"></div>
  <div class="nav-item" style="top:278px"><svg viewBox="0 0 10 10" fill="none" stroke="currentColor"><path d="M1 1v8h8M3 7V4M5 7V3M7 7V5"/></svg>Default Campaign</div>
  <div class="caret" style="top:285px"></div>
  <div class="hive-art" role="img" aria-label="Decorative honeycomb pattern in orange tones"></div>
</aside>

<h1 class="page-title">Home</h1>
<div class="welcome"><span class="avatar"></span><div><small>WELCOME</small><strong>Mara Quint</strong></div></div>

<div class="heading" style="left:245px;top:74px"><svg viewBox="0 0 14 14" fill="none" stroke="currentColor"><circle cx="4" cy="4" r="2"/><circle cx="10" cy="4" r="2"/><circle cx="7" cy="7.5" r="2"/><path d="M3 13a4 4 0 0 1 8 0"/></svg>Teamspace</div>
<section class="card team-card"><div class="card-title">Default</div><p>The default client is created as part of your user account.</p></section>

<div class="heading" style="left:245px;top:199px"><svg viewBox="0 0 14 14" fill="none" stroke="currentColor"><path d="M1 1v12h12M4 10V6M7 10V4M10 10V7"/></svg>Subscription Overview</div>
<section class="card usage-card"><div class="card-title">Starter Pack Usage</div><div class="usage-track"><div class="usage-fill"></div></div><div class="usage-note">0 Files active of 10 allowed</div></section>

<div class="heading" style="left:846px;top:200px"><svg viewBox="0 0 14 14" fill="none" stroke="currentColor"><rect x="3" y="3" width="7" height="10"/><path d="M5 1h6v9"/></svg>Files &amp; HoneyTokens</div>
<section class="card stats-card"><div class="card-title">Statistics</div>
  <div class="stat" style="left:29px"><div class="stat-num">30</div><div class="stat-label">Files</div></div>
  <div class="stat" style="left:173px"><div class="stat-num">0</div><div class="stat-label">HoneyTokens</div></div>
</section>

<div class="heading" style="left:247px;top:396px"><svg viewBox="0 0 14 14" fill="none" stroke="currentColor"><path d="M2 5h3l6-3v10L5 9H2zM5 9l1 3"/></svg>Campaigns</div>
<div class="new-btn">+ New Campaign</div>
<div class="campaign-panel"></div>

<article class="campaign" style="left:361px">
  <h3>My Custom Campaign</h3>
  <p class="desc">This is my custom campaign for finding i...</p>
  <div class="campaign-art" role="img" aria-label="Illustration of a bee on a flower"></div>
  <div class="campaign-count"><span class="num">0</span><span class="txt"><small>Active</small><strong>Files &amp; HoneyTokens</strong></span></div>
  <p class="since">Active since: Jul 25 2023 13:12</p>
</article>
<article class="campaign" style="left:756px">
  <h3>Default Campaign</h3>
  <p class="desc">Define your own mission, or combine differen...</p>
  <div class="campaign-art" role="img" aria-label="Illustration of a bee beside honeycomb cells"></div>
  <div class="campaign-count"><span class="num">0</span><span class="txt"><small>Active</small><strong>Files &amp; HoneyTokens</strong></span></div>
  <p class="since">Active since: Jul 25 2023 13:12</p>
</article>
</body>
</html>
```